Velmora Canvas - Portrait Oil Paintings from Photographs

To accompany my newly designed website, i am in need of a good flyer design promoting the service we actually provide.
Emphasis on all art works - 100% Hand painted by real life artists. Photo/painting editing available free.
Photos can be provided, "From this...to this" pictures available. Logo available.
A brief out line what we do, how we do it etc etc
Step by step process of of how to carry out your purchase "Let us paint your picture in 3 simple steps" 1. Upload your photo 2. Let us hand paint your masterpiece 3. Delivered direct to your door.
Web address, www.velmoracanvas.co (not yet online)
In regards to size, i am open to suggestions and ideas. So please feel free to submit accordingly what youre able to offer. I do like the idea of a folded piece of A4 (4 pages total?)

```html
<!DOCTYPE html>
<html lang="en">
<head>
<meta charset="utf-8">
<title>Velmora Canvas – Flyer</title>
<link rel="stylesheet" href="https://fonts.googleapis.com/css2?family=Alfa+Slab+One&family=Cinzel:wght@400;700&display=swap">
<style>
  :root {
    --paper: #ebe3cf;
    --paper-strip: #b8b1a2;
    --paper-strip-dark: #a59e8f;
    --crimson: #9c1c1c;
    --crimson-dark: #7d1414;
    --ink: #141414;
    --white: #ffffff;
    --footer-red: #a3221c;
    --frame: #f7f5f0;
  }
  * { margin: 0; padding: 0; box-sizing: border-box; }
  html, body { width: 847px; height: 1200px; overflow: hidden; background: var(--paper); }
  .flyer {
    position: relative;
    width: 847px;
    height: 1200px;
    overflow: hidden;
    background: var(--paper);
    font-family: "Cinzel", serif;
  }
  .layer { position: absolute; left: 0; top: 0; }

  .headline {
    position: absolute;
    left: 38px;
    top: 112px;
    color: var(--white);
    font-family: "Cinzel", serif;
    font-weight: 400;
    font-size: 40px;
    line-height: 1.25;
    letter-spacing: 1px;
    text-shadow: 0 1px 2px rgba(0,0,0,0.25);
  }
  .headline .cap { font-size: 50px; }

  .photo {
    position: absolute;
    background: var(--frame);
    padding: 12px;
    box-shadow: 2px 4px 10px rgba(0,0,0,0.45);
  }
  .photo .shot { width: 100%; height: 100%; }
  .photo--mother-child-a { left: 97px; top: 302px; width: 242px; height: 226px; transform: rotate(-3deg); }
  .photo--family-a { left: 322px; top: 240px; width: 302px; height: 254px; transform: rotate(-6deg); }
  .photo--family-b { left: 282px; top: 558px; width: 240px; height: 214px; transform: rotate(3deg); }
  .photo--mother-child-b { left: 505px; top: 505px; width: 252px; height: 252px; transform: rotate(7deg); }
  .photo--courier { left: 424px; top: 812px; width: 184px; height: 240px; transform: rotate(-9deg); }

  .shot--mother-child { background: linear-gradient(135deg, #6b5a4c 0%, #c7a68a 45%, #8f8a80 100%); }
  .shot--family { background: linear-gradient(160deg, #8a8f7a 0%, #c9a890 40%, #5d5d66 100%); }
  .shot--courier { background: linear-gradient(150deg, #e9e6df 0%, #d2b58e 50%, #a57a4c 100%); }

  .badge {
    position: absolute;
    width: 230px;
    height: 230px;
  }
  .badge svg { position: absolute; left: 0; top: 0; }
  .badge__text {
    position: absolute;
    inset: 0;
    display: flex;
    align-items: center;
    justify-content: center;
    text-align: center;
    color: var(--white);
    font-family: "Alfa Slab One", serif;
    font-size: 27px;
    line-height: 1.02;
    text-transform: uppercase;
    letter-spacing: 0.5px;
  }
  .badge--upload { left: 571px; top: 203px; transform: rotate(4deg); }
  .badge--paint { left: 67px; top: 540px; }
  .badge--paint .badge__text { font-size: 18px; letter-spacing: 0; line-height: 1.05; }
  .badge--deliver { left: 581px; top: 762px; }
  .badge--deliver .badge__text { font-size: 20px; }

  .promise-band {
    position: absolute;
    left: 0;
    top: 812px;
    width: 515px;
    height: 196px;
    background: var(--ink);
  }
  .promise {
    position: absolute;
    left: 40px;
    top: 826px;
    color: var(--white);
    font-family: "Cinzel", serif;
    font-weight: 400;
    line-height: 1;
    text-transform: uppercase;
  }
  .promise__big { display: block; font-size: 38px; margin-bottom: 6px; }
  .promise__line { display: block; font-size: 42px; margin-bottom: 4px; }

  .contact {
    position: absolute;
    left: 40px;
    top: 1050px;
    color: var(--footer-red);
    font-family: "Cinzel", serif;
    text-transform: uppercase;
    line-height: 1.3;
  }
  .contact__label { display: block; font-size: 24px; font-weight: 400; }
  .contact__email { display: block; font-size: 21px; font-weight: 700; }
  .contact__web { display: block; font-size: 20px; font-weight: 400; letter-spacing: 3px; }

  .brand {
    position: absolute;
    left: 488px;
    top: 1082px;
    display: flex;
    align-items: center;
    gap: 12px;
  }
  .brand__dot {
    width: 40px;
    height: 40px;
    border-radius: 50%;
    background: var(--footer-red);
  }
  .brand__name {
    color: var(--footer-red);
    font-family: "Cinzel", serif;
    font-weight: 700;
    font-size: 27px;
    white-space: nowrap;
  }
</style>
</head>
<body>
<main class="flyer">

  <svg class="layer" width="847" height="300" viewBox="0 0 847 300">
    <defs>
      <linearGradient id="wash" x1="0" y1="0" x2="1" y2="0">
        <stop offset="0" stop-color="#b5483a"/>
        <stop offset="0.35" stop-color="#c9a58a"/>
        <stop offset="0.6" stop-color="#6f8a52"/>
        <stop offset="1" stop-color="#9c2a24"/>
      </linearGradient>
    </defs>
    <rect role="img" aria-label="Painterly red and green watercolour texture" x="0" y="0" width="847" height="90" fill="url(#wash)"/>
    <polygon fill="var(--paper-strip)" points="0,30 60,40 120,28 200,42 260,26 330,44 400,30 470,46 540,32 610,44 680,26 750,40 847,30 847,232 790,238 720,226 650,240 560,230 470,244 380,228 300,242 210,230 130,244 60,232 0,240"/>
    <polyline fill="none" stroke="var(--paper-strip-dark)" stroke-width="3" points="0,30 60,40 120,28 200,42 260,26 330,44 400,30 470,46 540,32 610,44 680,26 750,40 847,30"/>
  </svg>

  <svg class="layer" width="847" height="760" viewBox="0 0 847 760">
    <polygon fill="var(--crimson)" points="0,250 70,240 150,256 230,236 310,250 400,232 500,246 600,226 700,238 780,220 847,230 847,600 800,612 790,680 720,690 640,670 560,686 470,668 380,690 290,676 200,694 120,676 40,690 0,682"/>
    <polygon fill="var(--crimson-dark)" opacity="0.35" points="0,560 120,540 260,570 420,546 600,572 800,548 847,560 847,600 800,612 790,680 720,690 640,670 560,686 470,668 380,690 290,676 200,694 120,676 40,690 0,682"/>
  </svg>

  <h1 class="headline"><span class="cap">L</span>et us paint your picture<br>in 3 simple steps</h1>

  <figure class="photo photo--mother-child-a"><div class="shot shot--mother-child" role="img" aria-label="Photograph of a mother with her young child"></div></figure>
  <figure class="photo photo--family-a"><div class="shot shot--family" role="img" aria-label="Photograph of a multi-generation family group"></div></figure>

  <div class="badge badge--upload">
    <svg width="230" height="230" viewBox="-115 -115 230 230" aria-hidden="true">
      <circle r="102" fill="var(--ink)"/>
      <circle r="106" fill="none" stroke="var(--ink)" stroke-width="12" stroke-dasharray="9 7"/>
      <circle r="90" fill="none" stroke="var(--white)" stroke-width="2"/>
      <circle r="84" fill="none" stroke="var(--white)" stroke-width="1"/>
    </svg>
    <p class="badge__text">Upload<br>your<br>photo</p>
  </div>

  <div class="badge badge--paint">
    <svg width="230" height="230" viewBox="-115 -115 230 230" aria-hidden="true">
      <circle r="102" fill="var(--ink)"/>
      <circle r="106" fill="none" stroke="var(--ink)" stroke-width="12" stroke-dasharray="9 7"/>
      <circle r="90" fill="none" stroke="var(--white)" stroke-width="2"/>
      <circle r="84" fill="none" stroke="var(--white)" stroke-width="1"/>
    </svg>
    <p class="badge__text">Let us<br>hand paint<br>your<br>masterpiece</p>
  </div>

  <figure class="photo photo--family-b"><div class="shot shot--family" role="img" aria-label="Hand-painted portrait of the family group"></div></figure>
  <figure class="photo photo--mother-child-b"><div class="shot shot--mother-child" role="img" aria-label="Hand-painted portrait of the mother and child"></div></figure>

  <div class="promise-band"></div>
  <p class="promise">
    <span class="promise__big">100%</span>
    <span class="promise__line">Hand painted</span>
    <span class="promise__line">by real life</span>
    <span class="promise__line">artists</span>
  </p>

  <figure class="photo photo--courier"><div class="shot shot--courier" role="img" aria-label="Photograph of a courier carrying parcels"></div></figure>

  <div class="badge badge--deliver">
    <svg width="230" height="230" viewBox="-115 -115 230 230" aria-hidden="true">
      <circle r="102" fill="var(--ink)"/>
      <circle r="106" fill="none" stroke="var(--ink)" stroke-width="12" stroke-dasharray="9 7"/>
      <circle r="90" fill="none" stroke="var(--white)" stroke-width="2"/>
      <circle r="84" fill="none" stroke="var(--white)" stroke-width="1"/>
    </svg>
    <p class="badge__text">Delivered<br>direct to<br>your door</p>
  </div>

  <footer class="contact">
    <span class="contact__label">For any queries</span>
    <span class="contact__email">support@velmoracanvas.co</span>
    <span class="contact__web">www.velmoracanvas.co</span>
  </footer>

  <div class="brand">
    <span class="brand__dot"></span>
    <span class="brand__name">Velmora Canvas</span>
  </div>

</main>
</body>
</html>
```